Safety Training company business card design

We are after a high quality, professional business card. We are open to a single or double sided card.

The winning designer must provide the card in a format where we can easily change the name and details of the different people in our organization.

Harbor Guard's company colour is lime green.

We provide all aspects of safety advisory and training for the Building, Civil Construction, Mining, Oil and Gas, Manufacturing, Rail, Rural and Retail sectors.

Visit our website www.harborguard.com.au for training competencies we offer along with our other services including RPL's, safety audits, professional development and client support.

Target Market(s)

Those in the Building, Civil Construction, Mining, Oil and Gas, Manufacturing, Rail, Rural and Retail industries.

Industry/Entity Type

Training

Contact Information for Business Card

Harbor Guard
Safety and Training
Dennis Palworth
Director
M 0427 518 266
dennis@harborguard.com.au
www.harborguard.com.au
(2 business addresses:)
Corvin High Risk Training Centre
17 Tandem Parade, Kellmore Q 4218 P 3912 5486 F 3912 5174
Brenlow Training Centre
86 Fenwick Street, Brenlow Q 4751 P 4873 2615 F 4873 2249

Colors
9bcb3c

Requirements
Must have
• Lime green must be the main colour. must include HG logo attached, and state Harbor Guard (Safety and Training in smaller/different font).

State something along the lines of:

Nice to have
• We offer remote training and we can come to you.

```html
<!DOCTYPE html>
<html lang="en">
<head>
<meta charset="utf-8">
<title>Harbor Guard – Business Card</title>
<link rel="stylesheet" href="https://fonts.googleapis.com/css2?family=Mulish:wght@700&family=Questrial&family=Roboto+Condensed:wght@700&display=swap">
<style>
  :root {
    --lime: #8cff00;
    --frame: #4cf52e;
    --white: #ffffff;
    --paper: #ffffff;
    --shadow: rgba(0, 0, 0, 0.45);
  }
  * { box-sizing: border-box; margin: 0; padding: 0; }
  html, body {
    width: 1200px;
    height: 694px;
    overflow: hidden;
    background: var(--paper);
  }
  .stage {
    position: relative;
    width: 1200px;
    height: 694px;
    border: 2px solid var(--frame);
    background: var(--paper);
  }
  .card {
    position: absolute;
    top: 161px;
    height: 317px;
    background: var(--white);
    box-shadow: 0 4px 18px var(--shadow);
    overflow: hidden;
  }
  .card--front { left: 80px; width: 500px; }
  .card--back  { left: 616px; width: 520px; }

  /* Front */
  .brand-panel {
    position: absolute;
    left: 0; top: 0;
    width: 237px; height: 100%;
    background: var(--white);
  }
  .brand-mark {
    position: absolute;
    left: 0; right: 0; top: 82px;
    text-align: center;
    font-family: "Roboto Condensed", "Arial Narrow", sans-serif;
    font-weight: 700;
    font-size: 38px;
    color: var(--lime);
    letter-spacing: 1px;
  }
  .brand-name {
    position: absolute;
    left: 0; right: 0; top: 149px;
    text-align: center;
    font-family: "Roboto Condensed", "Arial Narrow", sans-serif;
    font-weight: 700;
    font-size: 21px;
    color: var(--lime);
    white-space: nowrap;
  }
  .person-panel {
    position: absolute;
    left: 237px; top: 0;
    width: 263px; height: 100%;
    background: var(--lime);
    color: var(--white);
  }
  .person-name {
    position: absolute;
    left: 0; right: 0; top: 128px;
    text-align: center;
    font-family: "Mulish", Verdana, sans-serif;
    font-weight: 700;
    font-size: 21px;
  }
  .person-role {
    position: absolute;
    left: 0; right: 0; top: 159px;
    text-align: center;
    font-family: "Questrial", "Century Gothic", sans-serif;
    font-size: 15px;
    letter-spacing: 0.5px;
  }
  .contact-list {
    position: absolute;
    right: 13px; bottom: 10px;
    list-style: none;
    text-align: right;
    font-family: "Questrial", "Century Gothic", sans-serif;
    font-size: 13.5px;
    line-height: 17.5px;
    white-space: nowrap;
  }

  /* Back */
  .site-band {
    position: absolute;
    left: 0; top: 0;
    width: 100%; height: 170px;
    background: var(--lime);
  }
  .site {
    position: absolute;
    font-family: "Mulish", Verdana, sans-serif;
    font-weight: 700;
    font-size: 17px;
    line-height: 22.5px;
    font-style: normal;
    white-space: nowrap;
  }
  .site--north { left: 265px; top: 13px; color: var(--white); }
  .site--south { left: 20px; top: 198px; color: var(--lime); }
</style>
</head>
<body>
<main class="stage">
  <section class="card card--front" aria-label="Business card front">
    <div class="brand-panel">
      <div class="brand-mark">HG</div>
      <div class="brand-name">Harbor Guard and Training</div>
    </div>
    <div class="person-panel">
      <h1 class="person-name">Dennis Palworth</h1>
      <p class="person-role">Director</p>
      <ul class="contact-list">
        <li>M: 0427518266</li>
        <li>Web: www.harborguard.com.au</li>
        <li>Email: dennis@harborguard.com.au</li>
      </ul>
    </div>
  </section>

  <section class="card card--back" aria-label="Business card back">
    <div class="site-band"></div>
    <address class="site site--north">
      Brenlow Training Centre<br>
      86 Fenwick Street<br>
      Brenlow Q 4751<br>
      P: 48732615<br>
      F: 48732249
    </address>
    <address class="site site--south">
      Corvin High Risk Training Centre<br>
      17 Tandem Parade<br>
      Kellmore Q 4218<br>
      P: 39125486<br>
      F: 39125174
    </address>
  </section>
</main>
</body>
</html>
```